Business Card design for construction company

I would like a business card design for a construction company - Harlow Constructions. I have attached the ai logo file for use. I would like the card to be very smart and clean and incorporate only white and the two colours in the logo. I would like the card to have two sides. One side can just have the logo, the other with the relevant information.

Target Market(s)

Building and Construction Clients

Industry/Entity Type

Business

Contact Information for Business Card

Name: Tom Pardoe
Company: Harlow Constructions Pty Limited
Address: 14 Mallee Crescent Carrow Vale 2093
Phone: 0427 531 068
Email: tomp@harlowbuild-example.com.au

Font styles to use
Serif
Sans Serif

Requirements
Must have
• Details noted above
• Logo as provided
• Colours as in logo
• Square edges
• A font that compliments the logo
Should not have
• Any colour other than white and those in logo
• Rounded edges

```html
<!DOCTYPE html>
<html lang="en">
<head>
<meta charset="utf-8">
<title>Harlow Constructions — Business Card Front</title>
<link rel="stylesheet" href="https://fonts.googleapis.com/css2?family=Michroma&display=swap">
<style>
  :root {
    --card-bg: #f9f6f3;
    --brand-blue: #00adef;
    --brand-grey: #58585a;
  }
  html, body {
    margin: 0;
    padding: 0;
    width: 1200px;
    height: 720px;
    overflow: hidden;
    background: var(--card-bg);
  }
  .card {
    position: relative;
    width: 1200px;
    height: 720px;
    background: var(--card-bg);
    overflow: hidden;
  }
  .rule {
    position: absolute;
    background: var(--brand-blue);
  }
  .rule--top    { left: 0;     top: 79px;  width: 779px; height: 10px; }
  .rule--left   { left: 79px;  top: 0;     width: 10px;  height: 541px; }
  .rule--right  { left: 1111px; top: 179px; width: 10px; height: 541px; }
  .rule--bottom { left: 417px; top: 631px; width: 783px; height: 10px; }

  .wordmark {
    position: absolute;
    left: 0;
    top: 0;
    width: 1200px;
    height: 720px;
    display: flex;
    align-items: center;
    justify-content: center;
  }
  .wordmark__name {
    margin: 0;
    font-family: "Michroma", sans-serif;
    font-weight: 400;
    font-size: 26px;
    letter-spacing: 0.08em;
    text-transform: uppercase;
    color: var(--brand-grey);
    white-space: nowrap;
  }
</style>
</head>
<body>
  <main class="card">
    <div class="rule rule--top"></div>
    <div class="rule rule--left"></div>
    <div class="rule rule--right"></div>
    <div class="rule rule--bottom"></div>
    <div class="wordmark">
      <h1 class="wordmark__name">Harlow Constructions</h1>
    </div>
  </main>
</body>
</html>
```